Building company business card

Design and print business cards for BRENTHOLM PTY LTD.
A residantial homes building company.
Mark Lantern already designed the company Logo.

```html
<!DOCTYPE html>
<html lang="en">
<head>
<meta charset="utf-8">
<title>BRENTHOLM PTY LTD – Business Card</title>
<link href="https://fonts.googleapis.com/css2?family=Oswald:wght@600&family=Open+Sans:wght@400;600&display=swap" rel="stylesheet">
<style>
  :root {
    --stage: #1f1f1f;
    --navy: #11226e;
    --gold: #d9a63c;
    --white: #ffffff;
    --ink: #2a2a2a;
  }
  * { margin: 0; padding: 0; box-sizing: border-box; }
  html, body { width: 1200px; height: 1015px; overflow: hidden; }
  body { background: var(--stage); position: relative; font-family: "Open Sans", sans-serif; }

  .card {
    position: absolute;
    width: 560px;
    height: 320px;
    overflow: hidden;
    box-shadow: 0 14px 30px rgba(0,0,0,.55);
  }

  /* Front */
  .card--front { left: 80px; top: 90px; background: var(--navy); display: flex; align-items: center; justify-content: center; gap: 16px; }
  .front__square { width: 26px; height: 26px; background: var(--gold); }
  .front__name { font-family: "Oswald", sans-serif; font-weight: 600; font-size: 64px; color: var(--white); letter-spacing: 1px; }

  /* Back */
  .card--back { left: 560px; top: 580px; background: var(--white); }
  .back__brand { position: absolute; right: 34px; top: 26px; font-family: "Oswald", sans-serif; font-weight: 600; font-size: 44px; color: var(--navy); letter-spacing: .5px; }
  .person { position: absolute; left: 34px; top: 100px; }
  .person__name { font-family: "Oswald", sans-serif; font-weight: 600; font-size: 22px; color: var(--navy); }
  .person__role { font-size: 13px; color: var(--ink); margin-top: -2px; }
  .registration { position: absolute; left: 34px; top: 158px; font-size: 12px; line-height: 16px; color: var(--navy); }

  .band { position: absolute; left: 0; bottom: 0; width: 100%; height: 118px; background: var(--navy); }
  .contacts { position: absolute; left: 34px; top: 16px; list-style: none; }
  .contacts li { display: flex; align-items: center; gap: 9px; font-size: 12.5px; line-height: 21px; color: var(--white); }
  .contacts svg { width: 13px; height: 13px; flex: none; }
  .office { position: absolute; right: 34px; top: 20px; text-align: right; font-size: 12.5px; line-height: 19px; color: var(--white); }
  .office__name { color: var(--gold); font-weight: 600; }
</style>
</head>
<body>

  <section class="card card--front">
    <span class="front__square"></span>
    <span class="front__name">BRENTHOLM</span>
  </section>

  <section class="card card--back">
    <div class="back__brand">BRENTHOLM</div>

    <div class="person">
      <div class="person__name">DORIAN (Dory) KESTREL</div>
      <div class="person__role">Director</div>
    </div>

    <div class="registration">
      <div>ABN- 48 210 936 157</div>
      <div>CDB-U 41856</div>
    </div>

    <div class="band">
      <ul class="contacts">
        <li>
          <svg viewBox="0 0 16 16"><path fill="var(--gold)" d="M3.5 1.5l2.6 2.7-1.5 1.8c.9 2 2.4 3.5 4.4 4.4l1.8-1.5 2.7 2.6-1.7 2.2C6.8 13.5 2.5 9.2 1.3 3.2z"/></svg>
          0412 555 087
        </li>
        <li>
          <svg viewBox="0 0 16 16"><rect x="4" y="1" width="8" height="14" rx="1.5" fill="none" stroke="var(--gold)" stroke-width="1.6"/><circle cx="8" cy="12.5" r="0.9" fill="var(--gold)"/></svg>
          0438 555 214
        </li>
        <li>
          <svg viewBox="0 0 16 16"><rect x="1" y="3" width="14" height="10" fill="var(--gold)"/><path d="M1 3l7 6 7-6" fill="none" stroke="var(--navy)" stroke-width="1.3"/></svg>
          dk@brentholm-pl.com
        </li>
        <li>
          <svg viewBox="0 0 16 16" fill="none" stroke="var(--gold)" stroke-width="1.3"><circle cx="8" cy="8" r="6.5"/><ellipse cx="8" cy="8" rx="3" ry="6.5"/><path d="M1.5 8h13M2.5 4.8h11M2.5 11.2h11"/></svg>
          www.brentholm-pl.com
        </li>
      </ul>

      <address class="office" style="font-style:normal">
        <div class="office__name">BRENTHOLM PTY LTD</div>
        <div>PO Box 482</div>
        <div>Elmridge Vic 3199</div>
      </address>
    </div>
  </section>

</body>
</html>
```